Leaf Haven Business Card Design

My E-Commerce store is called Leaf Haven

Website address is - http://www.leafhaven-demo.com.au

I would like a colourful, friendly business with the description in the 'must haves' box incorporated into it
Updates

Please add the following to the business cards; Natural & Organic Products Online Organic Pantry Items Superfoods & Supplements Natural Skincare Eco Friendly Household Products

Industry/Entity Type

Business

Contact Information for Business Card

www.leafhaven-demo.com.au
mira@leafhaven-demo.com.au

Colors
acd037
9bcb3c
cadf82
eaf2ce

Requirements
Must have
• Natural & Organic Eco Products Online.
• Leaf Haven specialises in organic pantry items, superfoods and supplements, organic skincare for you and your family & eco friendly household products.

```html
<!DOCTYPE html>
<html lang="en">
<head>
<meta charset="utf-8">
<title>Leaf Haven – Business Card</title>
<link rel="stylesheet" href="https://fonts.googleapis.com/css2?family=Quicksand:wght@500;600;700&family=Nunito:ital,wght@0,700;0,800;1,700;1,800&display=swap">
<style>
  :root {
    --backdrop: #303431;
    --card: #f7f8f6;
    --card-edge: #e6e9e5;
    --green: #1f9a3c;
    --green-mid: #3fae4a;
    --green-light: #8fcf6a;
    --text-font: "Nunito", sans-serif;
    --brand-font: "Quicksand", sans-serif;
  }
  html, body {
    margin: 0;
    width: 1200px;
    height: 800px;
    overflow: hidden;
    background: var(--backdrop);
  }
  .stage {
    position: relative;
    width: 1200px;
    height: 800px;
    display: flex;
    align-items: center;
    justify-content: center;
    gap: 40px;
  }
  .card {
    position: relative;
    width: 540px;
    height: 310px;
    background: var(--card);
    border-radius: 14px;
    box-shadow: 0 18px 40px rgba(0,0,0,0.35);
    overflow: hidden;
    color: var(--green);
    font-family: var(--text-font);
  }

  /* Brand name block */
  .brand {
    display: flex;
    align-items: center;
    gap: 14px;
  }
  .brand-dot {
    width: 44px;
    height: 44px;
    border-radius: 50%;
    background: var(--green-mid);
    flex: none;
  }
  .brand-name {
    font-family: var(--brand-font);
    font-weight: 600;
    font-size: 40px;
    color: var(--green);
    line-height: 1;
    white-space: nowrap;
  }

  /* Front */
  .card-front .brand {
    position: absolute;
    left: 30px;
    top: 110px;
  }
  .offer-list {
    position: absolute;
    right: 30px;
    top: 36px;
    margin: 0;
    padding: 0;
    list-style: none;
    text-align: right;
    font-weight: 800;
    font-size: 21px;
    line-height: 1.35;
    letter-spacing: 0.3px;
  }
  .divider {
    position: absolute;
    right: 30px;
    top: 178px;
    width: 200px;
    height: 1.5px;
    background: var(--green-mid);
  }
  .contact {
    position: absolute;
    right: 30px;
    top: 192px;
    margin: 0;
    padding: 0;
    list-style: none;
    font-weight: 700;
    font-size: 14px;
    line-height: 1.9;
  }
  .contact li {
    display: flex;
    align-items: center;
    gap: 10px;
  }
  .contact svg { width: 16px; height: 16px; flex: none; }
  .shipping-note {
    position: absolute;
    left: 30px;
    right: 30px;
    bottom: 20px;
    margin: 0;
    font-weight: 800;
    font-size: 10.5px;
    text-transform: uppercase;
    line-height: 1.35;
    color: var(--green-mid);
    text-align: right;
  }

  /* Back */
  .tagline {
    position: absolute;
    left: 32px;
    top: 56px;
    margin: 0;
    font-style: italic;
    font-size: 22px;
    line-height: 1.2;
  }
  .tagline strong { font-weight: 800; display: block; }
  .tagline span { font-weight: 700; display: block; }
  .card-back .brand {
    position: absolute;
    right: 34px;
    bottom: 70px;
  }
</style>
</head>
<body>
<main class="stage">

  <section class="card card-front" aria-label="Business card front">
    <div class="brand">
      <span class="brand-dot" aria-hidden="true"></span>
      <span class="brand-name">Leaf Haven</span>
    </div>

    <ul class="offer-list">
      <li>ECO BABY &amp; KIDS</li>
      <li>ECO BODY</li>
      <li>ECO PANTRY</li>
      <li>ECO HOME</li>
    </ul>

    <div class="divider"></div>

    <ul class="contact">
      <li>
        <svg viewBox="0 0 16 16" aria-hidden="true">
          <rect x="1" y="3" width="14" height="10" rx="1" fill="none" stroke="#1f9a3c" stroke-width="1.5"/>
          <path d="M1.5 3.5 L8 9 L14.5 3.5" fill="none" stroke="#1f9a3c" stroke-width="1.5"/>
        </svg>
        mira@leafhaven-demo.com.au
      </li>
      <li>
        <svg viewBox="0 0 16 16" aria-hidden="true">
          <circle cx="8" cy="8" r="6.5" fill="none" stroke="#1f9a3c" stroke-width="1.5"/>
          <ellipse cx="8" cy="8" rx="2.8" ry="6.5" fill="none" stroke="#1f9a3c" stroke-width="1.2"/>
          <line x1="1.5" y1="8" x2="14.5" y2="8" stroke="#1f9a3c" stroke-width="1.2"/>
        </svg>
        www.leafhaven-demo.com.au
      </li>
    </ul>

    <p class="shipping-note">Shipping is charged at a flat rate of $11.50 per order.<br>Free shipping on orders over $100!</p>
  </section>

  <section class="card card-back" aria-label="Business card back">
    <p class="tagline">
      <strong>Natural &amp; Organic</strong>
      <span>Eco Product</span>
    </p>
    <div class="brand">
      <span class="brand-dot" aria-hidden="true"></span>
      <span class="brand-name">Leaf Haven</span>
    </div>
  </section>

</main>
</body>
</html>
```